NEW Modern Sleek Business Card for VR Language Startup

Our startup is using VR to lead the next wave of world language education. We need a two-sided business card that introduces the larger organization (Brightvale Tongues Inc) and our contact info on one side and shows the product, Lexiquorra, on the other side.

Side 1 (contact info)= Brightvale Logo and Contact info (name, title, phone, email)

Side 2 (product)= Lexiquora logo, text, and website
Text= Culturally Immersive Language Learning Games
Website= www.lexiquora-demo.test

Target Market(s)

Education, Technology

Contact Information for Business Card

Contact info will be updated upon approval of the design. For now, put this as a placeholder.

Peter Hallow
Founder & CEO
phallow@mailbox-demo.test
(555)-010-4477

Font styles to use
Other font styles liked:
• Gibson and Century Gothic are the brand fonts

Requirements
Nice to have
• I would love to see cohesion between the design and colors of the two logos. I have attached a few business card designs that I like, so you can get a feel for my preferred style.

```html
<!DOCTYPE html>
<html lang="en">
<head>
<meta charset="utf-8">
<title>Brightvale Tongues Inc – Business Card</title>
<link rel="stylesheet" href="https://fonts.googleapis.com/css2?family=Didact+Gothic&family=Montserrat:wght@600;700&display=swap">
<style>
  :root {
    --page-bg: #3a3a3c;
    --white: #ffffff;
    --ink: #4a4a4c;
    --ink-soft: #555558;
    --band-teal: #5ccad6;
    --band-sky: #34bdee;
    --band-indigo: #5e6ab0;
  }
  * { margin: 0; padding: 0; box-sizing: border-box; }
  html, body { width: 984px; height: 1200px; overflow: hidden; }
  body { background: var(--page-bg); position: relative; font-family: "Didact Gothic", "Century Gothic", sans-serif; }

  .card { position: absolute; left: 171px; width: 642px; height: 415px; border-radius: 38px; overflow: hidden; }
  .card-front { top: 158px; }
  .card-back { top: 626px; background: var(--white); }
  .card-art { position: absolute; inset: 0; width: 100%; height: 100%; }

  .contact-header { position: absolute; top: 34px; left: 0; width: 100%; display: flex; align-items: baseline; justify-content: center; gap: 26px; color: var(--white); white-space: nowrap; }
  .contact-name { font-family: "Montserrat", sans-serif; font-weight: 700; font-size: 18px; letter-spacing: 8px; }
  .contact-title { font-family: "Didact Gothic", sans-serif; font-weight: 400; font-size: 13px; letter-spacing: 5px; }

  .brand-front { position: absolute; top: 163px; left: 0; width: 100%; display: flex; align-items: center; justify-content: center; gap: 22px; }
  .brand-mark { width: 96px; height: 96px; border-radius: 50%; background: var(--white); }
  .brand-name { color: var(--white); font-family: "Montserrat", sans-serif; font-weight: 700; font-size: 44px; letter-spacing: 4px; text-transform: uppercase; }

  .contact-footer { position: absolute; top: 364px; left: 0; width: 100%; display: flex; align-items: center; justify-content: center; gap: 26px; white-space: nowrap; }
  .contact-row { display: flex; align-items: center; gap: 12px; color: var(--white); font-size: 14px; letter-spacing: 3px; }
  .contact-icon { width: 24px; height: 24px; flex: none; }

  .product-mark { position: absolute; top: 127px; left: 265px; width: 112px; height: 112px; border-radius: 50%; background: linear-gradient(135deg, var(--band-sky), var(--band-indigo)); }
  .product-name { position: absolute; top: 244px; left: 0; width: 100%; text-align: center; color: var(--ink); font-family: "Didact Gothic", sans-serif; font-weight: 400; font-size: 42px; }
  .product-tagline { position: absolute; top: 298px; left: 0; width: 100%; text-align: center; color: var(--ink-soft); font-size: 14px; line-height: 21px; letter-spacing: 7px; text-transform: uppercase; white-space: nowrap; }
  .product-rule { position: absolute; top: 356px; left: 151px; width: 340px; height: 2px; background: linear-gradient(90deg, var(--band-teal), var(--band-sky), var(--band-indigo)); }
  .product-web { position: absolute; top: 370px; left: 0; width: 100%; display: flex; align-items: center; justify-content: center; gap: 20px; color: var(--ink); font-size: 15px; letter-spacing: 4px; white-space: nowrap; }
  .web-icon { width: 25px; height: 25px; flex: none; }
</style>
</head>
<body>

<section class="card card-front">
  <svg class="card-art" viewBox="0 0 642 415" aria-hidden="true">
    <defs>
      <linearGradient id="frontGradient" x1="0" y1="0" x2="1" y2="1">
        <stop offset="0" stop-color="#f8b133"/>
        <stop offset="0.3" stop-color="#ee2d45"/>
        <stop offset="0.52" stop-color="#a3338f"/>
        <stop offset="0.72" stop-color="#7a62ab"/>
        <stop offset="1" stop-color="#51c6d8"/>
      </linearGradient>
    </defs>
    <rect width="642" height="415" fill="url(#frontGradient)"/>
  </svg>

  <header class="contact-header">
    <h1 class="contact-name">PETER HALLOW</h1>
    <p class="contact-title">FOUNDER &amp; CEO</p>
  </header>

  <div class="brand-front">
    <span class="brand-mark"></span>
    <span class="brand-name">Brightvale</span>
  </div>

  <footer class="contact-footer">
    <p class="contact-row contact-email">
      <svg class="contact-icon" viewBox="0 0 24 24" aria-hidden="true">
        <circle cx="12" cy="12" r="12" fill="#fff"/>
        <rect x="6" y="8" width="12" height="8.5" rx="1" fill="none" stroke="#c23a78" stroke-width="1.4"/>
        <path d="M6.5 8.6 12 13l5.5-4.4" fill="none" stroke="#c23a78" stroke-width="1.4"/>
      </svg>
      phallow@mailbox-demo.test
    </p>
    <p class="contact-row contact-phone">
      <svg class="contact-icon" viewBox="0 0 24 24" aria-hidden="true">
        <circle cx="12" cy="12" r="12" fill="#fff"/>
        <path d="M8.2 6.5c.6-.4 1.3-.2 1.6.4l1 1.9c.3.5.1 1.1-.3 1.4l-.8.6c.6 1.5 1.7 2.7 3.1 3.4l.6-.8c.4-.4 1-.5 1.4-.2l1.9 1.1c.6.3.7 1.1.3 1.6l-.8.9c-.6.6-1.5.8-2.3.5-3.1-1.2-5.4-3.6-6.5-6.7-.3-.8 0-1.7.6-2.3z" fill="#8a5ca6"/>
      </svg>
      (555)-010-4477
    </p>
  </footer>
</section>

<section class="card card-back">
  <svg class="card-art" viewBox="0 0 642 415" aria-hidden="true">
    <defs>
      <linearGradient id="bandGradient" x1="0" y1="0" x2="1" y2="0.5">
        <stop offset="0" stop-color="#5ccad6"/>
        <stop offset="0.25" stop-color="#34bdee"/>
        <stop offset="0.7" stop-color="#5e6ab0"/>
        <stop offset="1" stop-color="#5e6ab0"/>
      </linearGradient>
    </defs>
    <path d="M0 0H642V128C610 70 550 40 470 39C380 38 300 70 230 105C160 140 90 175 40 166C20 162 8 157 0 152Z" fill="url(#bandGradient)"/>
  </svg>

  <span class="product-mark"></span>
  <h2 class="product-name">Lexiquora</h2>
  <p class="product-tagline">Culturally Immersive<br>Language Learning Games</p>
  <span class="product-rule"></span>
  <p class="product-web">
    <svg class="web-icon" viewBox="0 0 24 24" aria-hidden="true">
      <circle cx="12" cy="12" r="12" fill="#4a4a4c"/>
      <g fill="none" stroke="#fff" stroke-width="1">
        <circle cx="12" cy="12" r="6.5"/>
        <ellipse cx="12" cy="12" rx="3" ry="6.5"/>
        <path d="M5.5 12h13M6.5 8.5h11M6.5 15.5h11M12 5.5v13"/>
      </g>
    </svg>
    www.lexiquora-demo.test
  </p>
</section>

</body>
</html>
```